Live Band Music Series on Beach Flyer

Driftwood Cove Resort at Monterey Bay, California is introducing a Music Series "Tunes by the Tide", offering every Sunday starting April 16, 2023 from 2:30pm - 4:00PM. These are live bands performing for free on our beach. We would need the dates and times as well as our logo in a fun, family-oriented and beach/ wave/ cliff themed flyer. The phrase 'Surf’s Up!' can be included as well.
Event dates are April 16, April 23, April 30 and May 7 and information are available at our Event Calendar at driftwoodcoveresort.com
NOTE TO DESIGNER: Based on success we may extend throughout summer

```html
<!DOCTYPE html>
<html lang="en">
<head>
<meta charset="utf-8">
<title>Tunes by the Tide – Driftwood Cove Resort</title>
<link rel="stylesheet" href="https://fonts.googleapis.com/css2?family=EB+Garamond:wght@400;500&family=Kaushan+Script&family=Montserrat:wght@500;700&family=Open+Sans:wght@400&family=Nanum+Brush+Script&display=swap">
<style>
  :root {
    --sky-top: #4f7174;
    --sky-mid: #8a6a84;
    --sky-rose: #b8697c;
    --sky-peach: #e6a888;
    --sky-sand: #f3d49c;
    --sun-glow: #fff4cf;
    --palm-shade: rgba(38, 24, 62, 0.92);
    --palm-fade: rgba(38, 24, 62, 0);
    --ink-white: #ffffff;
    --ink-dark: #141414;
    --panel: rgba(27, 58, 79, 0.94);
    --panel-edge: #5f8d99;
    --panel-rule: #8fb0b8;
  }
  * { box-sizing: border-box; margin: 0; padding: 0; }
  html, body { width: 848px; height: 1200px; overflow: hidden; }
  body { background: var(--sky-top); }

  .flyer {
    position: relative;
    width: 848px;
    height: 1200px;
    overflow: hidden;
  }

  .flyer__sky {
    position: absolute;
    inset: 0;
    background:
      radial-gradient(circle at 815px 440px, var(--sun-glow) 0, rgba(255, 240, 200, 0.6) 50px, rgba(255, 230, 190, 0) 240px),
      linear-gradient(180deg, var(--sky-top) 0%, var(--sky-mid) 35%, var(--sky-rose) 52%, var(--sky-peach) 76%, var(--sky-sand) 88%, var(--sky-peach) 100%);
  }

  .flyer__palm {
    position: absolute;
    border-radius: 50%;
    background: radial-gradient(ellipse at center, var(--palm-shade) 0%, rgba(38, 24, 62, 0.7) 40%, var(--palm-fade) 72%);
  }
  .flyer__palm--left { left: -60px; top: 560px; width: 390px; height: 330px; }
  .flyer__palm--upper-right { left: 560px; top: -80px; width: 380px; height: 420px; }
  .flyer__palm--lower-right { left: 520px; top: 500px; width: 400px; height: 360px; opacity: 0.85; }

  .flyer__lights {
    position: absolute;
    left: 0;
    top: 0;
    width: 320px;
    height: 80px;
    background: radial-gradient(ellipse at 40% 30%, rgba(255, 236, 170, 0.45) 0%, rgba(255, 236, 170, 0) 70%);
  }

  .brand {
    position: absolute;
    top: 92px;
    left: 0;
    width: 100%;
    text-align: center;
    font-family: "EB Garamond", serif;
    font-weight: 400;
    font-size: 34px;
    color: var(--ink-white);
    letter-spacing: 0.5px;
  }

  .title {
    position: absolute;
    left: 70px;
    top: 282px;
    color: var(--ink-white);
    font-weight: normal;
    text-shadow: 3px 4px 6px rgba(40, 30, 60, 0.45);
  }
  .title__words { position: relative; display: inline-block; }
  .title__main {
    display: block;
    font-family: "EB Garamond", serif;
    font-weight: 500;
    font-size: 128px;
    letter-spacing: 5px;
    line-height: 1;
  }
  .title__link {
    display: block;
    margin-top: -14px;
    text-align: right;
    font-family: "Open Sans", sans-serif;
    font-weight: 400;
    font-size: 52px;
    line-height: 1;
  }
  .title__accent {
    position: absolute;
    left: 100%;
    bottom: -6px;
    margin-left: 6px;
    font-family: "Kaushan Script", cursive;
    font-size: 108px;
    line-height: 1;
    white-space: nowrap;
    transform: rotate(-6deg);
    transform-origin: left bottom;
  }

  .schedule {
    position: absolute;
    left: 244px;
    top: 726px;
    width: 361px;
    height: 202px;
    background: var(--panel);
    border: 2px solid var(--panel-edge);
    border-radius: 20px;
    color: var(--ink-white);
    font-family: "EB Garamond", serif;
    font-size: 27px;
    letter-spacing: 0.5px;
  }
  .schedule__dates {
    position: absolute;
    top: 20px;
    left: 22px;
    border-collapse: collapse;
  }
  .schedule__dates td { padding: 2px 0; line-height: 34px; }
  .schedule__divider { width: 42px; text-align: center; }
  .schedule__rule {
    position: absolute;
    left: 14px;
    right: 14px;
    top: 122px;
    height: 2px;
    background: var(--panel-rule);
  }
  .schedule__time {
    position: absolute;
    top: 138px;
    left: 60px;
  }

  .tagline {
    position: absolute;
    top: 1008px;
    left: 0;
    width: 100%;
    text-align: center;
    font-family: "Nanum Brush Script", cursive;
    font-size: 108px;
    color: var(--ink-dark);
    line-height: 1;
  }

  .info {
    position: absolute;
    top: 1120px;
    left: 0;
    width: 100%;
    text-align: center;
    font-family: "Montserrat", sans-serif;
    font-weight: 500;
    font-size: 19px;
    line-height: 27px;
    color: var(--ink-dark);
  }
  .info strong { font-weight: 700; }
</style>
</head>
<body>
  <main class="flyer">
    <div class="flyer__sky" role="img" aria-label="Beach sunset sky with glowing sun and sparkles"></div>
    <div class="flyer__lights" role="img" aria-label="String of warm party lights"></div>
    <div class="flyer__palm flyer__palm--upper-right" role="img" aria-label="Palm fronds silhouette"></div>
    <div class="flyer__palm flyer__palm--lower-right" role="img" aria-label="Palm tree silhouette"></div>
    <div class="flyer__palm flyer__palm--left" role="img" aria-label="Palm tree silhouette"></div>

    <p class="brand">Driftwood Cove Resort</p>

    <h1 class="title">
      <span class="title__words">
        <span class="title__main">TUNES</span>
        <span class="title__link">by the</span>
        <span class="title__accent">Tide</span>
      </span>
    </h1>

    <section class="schedule" aria-label="Event dates and time">
      <table class="schedule__dates">
        <tr><td>APRIL 16</td><td class="schedule__divider">|</td><td>APRIL 23</td></tr>
        <tr><td>APRIL 30</td><td class="schedule__divider">|</td><td>MAY 07</td></tr>
      </table>
      <div class="schedule__rule"></div>
      <p class="schedule__time">2:30PM - 4:00PM.</p>
    </section>

    <p class="tagline">Surf’s Up!</p>

    <p class="info">More information are available at<br>our Event Calendar at <strong>driftwoodcoveresort.com</strong></p>
  </main>
</body>
</html>
```